Dunmore Plumbing LLC business card

Would like a modern looking business card with my new logo

Contact Information for Business Card

Calvin Dunmore 2418 Elm Hollow Rd Brackenford, WX 06999, Dunmoreplumbingllc@exampletrade.com, 555-555-0174

```html
<!DOCTYPE html>
<html lang="en">
<head>
<meta charset="utf-8">
<title>Dunmore Plumbing LLC — Business Card</title>
<link href="https://fonts.googleapis.com/css2?family=Montserrat:wght@400;600;800&display=swap" rel="stylesheet">
<style>
  :root {
    --bg: #e9eaec;
    --card-white: #ffffff;
    --card-black: #161616;
    --card-black-light: #2a2a2a;
    --brand-blue: #12aaea;
    --ink: #1a1a1a;
    --text: #2b2b2b;
  }
  * { box-sizing: border-box; margin: 0; padding: 0; }
  html, body { width: 1200px; height: 1200px; overflow: hidden; }
  body {
    background: var(--bg);
    font-family: "Montserrat", sans-serif;
    position: relative;
  }
  .card {
    position: absolute;
    left: 220px;
    width: 760px;
    height: 434px;
    border-radius: 30px;
    overflow: hidden;
    box-shadow: 0 10px 30px rgba(0,0,0,0.18);
  }
  /* Front side */
  .card-front { top: 136px; background: var(--card-white); }
  .front-wordmark {
    position: absolute;
    right: 60px;
    top: 120px;
    display: flex;
    align-items: center;
    gap: 14px;
    color: var(--ink);
    font-weight: 800;
    font-size: 30px;
    letter-spacing: 1px;
    line-height: 1.1;
    text-transform: uppercase;
  }
  .wordmark-square {
    width: 22px; height: 22px;
    background: var(--brand-blue);
    flex: none;
  }
  .contact-block {
    position: absolute;
    left: 64px;
    top: 210px;
  }
  .person-name {
    color: var(--brand-blue);
    font-weight: 600;
    font-size: 36px;
    letter-spacing: 0.5px;
    text-transform: uppercase;
    margin-bottom: 14px;
  }
  .contact-list { list-style: none; }
  .contact-item {
    display: flex;
    align-items: flex-start;
    gap: 14px;
    color: var(--text);
    font-size: 18px;
    line-height: 1.3;
    margin-bottom: 6px;
  }
  .contact-icon { width: 18px; height: 18px; flex: none; margin-top: 3px; fill: var(--brand-blue); }
  .front-band-blue {
    position: absolute;
    left: 0; bottom: 0;
    width: 62%; height: 16px;
    background: var(--brand-blue);
    clip-path: polygon(0 0, 100% 0, 98% 100%, 0 100%);
  }
  .front-band-black {
    position: absolute;
    right: 0; bottom: 0;
    width: 37%; height: 34px;
    background: var(--ink);
    clip-path: polygon(3% 0, 100% 0, 100% 100%, 0 100%);
  }
  /* Back side */
  .card-back {
    top: 630px;
    background: radial-gradient(ellipse at 45% 45%, var(--card-black-light) 0%, var(--card-black) 70%);
  }
  .back-wordmark {
    position: absolute;
    left: 0; right: 0;
    top: 150px;
    display: flex;
    justify-content: center;
    align-items: center;
    gap: 18px;
    color: #ffffff;
    font-weight: 800;
    font-size: 44px;
    letter-spacing: 1.5px;
    text-transform: uppercase;
  }
  .back-wordmark .wordmark-square { width: 30px; height: 30px; }
  .back-band-blue {
    position: absolute;
    right: 0; bottom: 0;
    width: 52%; height: 40px;
    background: var(--brand-blue);
    border-top-left-radius: 26px;
  }
</style>
</head>
<body>
  <section class="card card-front">
    <div class="front-wordmark"><span class="wordmark-square"></span><span>Dunmore<br>Plumbing LLC</span></div>
    <div class="contact-block">
      <h1 class="person-name">Calvin Dunmore</h1>
      <ul class="contact-list">
        <li class="contact-item">
          <svg class="contact-icon" viewBox="0 0 24 24"><path d="M6.6 10.8a15.1 15.1 0 0 0 6.6 6.6l2.2-2.2a1 1 0 0 1 1-.25 11.4 11.4 0 0 0 3.6.57 1 1 0 0 1 1 1V20a1 1 0 0 1-1 1A17 17 0 0 1 3 4a1 1 0 0 1 1-1h3.5a1 1 0 0 1 1 1c0 1.25.2 2.45.57 3.57a1 1 0 0 1-.25 1z"/></svg>
          <span>555-555-0174</span>
        </li>
        <li class="contact-item">
          <svg class="contact-icon" viewBox="0 0 24 24"><path d="M2 5h20v14H2z M3.5 6.5 12 13l8.5-6.5" fill="var(--brand-blue)" stroke="#fff" stroke-width="1.4"/></svg>
          <span>Dunmoreplumbingllc@exampletrade.com</span>
        </li>
        <li class="contact-item">
          <svg class="contact-icon" viewBox="0 0 24 24"><path d="M12 2a7 7 0 0 0-7 7c0 5.2 7 13 7 13s7-7.8 7-13a7 7 0 0 0-7-7zm0 9.5A2.5 2.5 0 1 1 12 6.5a2.5 2.5 0 0 1 0 5z"/></svg>
          <span>2418 Elm Hollow Rd<br>Brackenford, WX 06999</span>
        </li>
      </ul>
    </div>
    <div class="front-band-blue"></div>
    <div class="front-band-black"></div>
  </section>

  <section class="card card-back">
    <div class="back-wordmark"><span class="wordmark-square"></span><span>Dunmore Plumbing LLC</span></div>
    <div class="back-band-blue"></div>
  </section>
</body>
</html>
```